Non-Profit focusing on clean water needs a poster/flyer design for our annual Stroll 2 Rivers

We need a poster and flyer design for our annual Stroll 2 Rivers event which will be held on Saturday, March 21st (Earthwide Thirst Day) at Merrow Fern Gardens.

HEAD:

Think Globally, Walk Locally.

SUB:

Join K7U in Santa Barbara on Earthwide Thirst Day for a Stroll 2 Rivers.

PHOTOS:

(one photo of past walk – crowd scene but with one face standing out – smaller photos of our team working out of country)

SUB:

Saturday, March 21st, 10am - 2pm

HEAD

Merrow Fern Gardens, Santa Barbara

COPY:

For more info check out our website: www.brightwellaid.org, or contact our Director: dana@brightwellaid.org; 805 382 9046

K7U Logo with Tag Line

NOTHING ELSE.

The final design should communicate fun for the whole family. Blue-ish shades to denote water. Be the generation that solves the world's water crisis.

Also, no need to use the attached photos if you can come up with a cool big idea graphic.

```html
<!DOCTYPE html>
<html lang="en">
<head>
<meta charset="utf-8">
<title>Stroll 2 Rivers — K7U</title>
<link href="https://fonts.googleapis.com/css2?family=Roboto:ital,wght@0,400;0,700;0,900;1,400;1,700&family=Roboto+Condensed:wght@400;700&display=swap" rel="stylesheet">
<style>
  :root{
    --page:#ececec;
    --paper:#ffffff;
    --panel:#f3f3f3;
    --ink:#3a3a3a;
    --sky:#2ba3e6;
    --navy:#2a2a6c;
    --walker-a:#3aa0e0;
    --walker-b:#24236a;
    --yellow:#f4c20d;
    --green:#3aa84a;
    --blue:#3b7de0;
    --red:#d41f1f;
    --brand-dot:#1c1c1c;
  }
  *{margin:0;padding:0;box-sizing:border-box}
  html,body{width:1200px;height:1000px;overflow:hidden;background:var(--page)}
  .flyer{
    position:absolute;left:268px;top:30px;width:664px;height:940px;
    background:var(--paper);overflow:hidden;
    box-shadow:0 2px 10px rgba(0,0,0,.18);
    font-family:"Roboto",sans-serif;color:var(--ink);
  }
  .photo{position:absolute}
  .photo-rope-line{left:0;top:0;width:664px;height:427px;
    background:linear-gradient(180deg,#5f8a4c 0%,#8aa3ad 18%,#6fa6d4 38%,#7d8fa6 55%,#a99a86 75%,#c5b9a8 100%)}
  .photo-crowd{left:274px;top:427px;width:390px;height:246px;
    background:linear-gradient(180deg,#8cc7ee 0%,#3d74c4 14%,#7f858d 30%,#8d8f93 70%,#6f7479 100%)}
  .photo-digging{left:0;top:673px;width:274px;height:267px;
    background:linear-gradient(180deg,#a89b8a 0%,#7a9ec4 35%,#b3a592 60%,#c6b8a4 100%)}

  .headline{position:absolute;right:12px;top:208px;text-align:right;
    font-family:"Roboto",sans-serif;font-weight:700;font-size:49px;line-height:1.0;
    color:#fff;text-shadow:0 2px 6px rgba(0,0,0,.45);letter-spacing:-.5px}
  .headline span{display:block}
  .headline .line-two{margin-top:6px}
  .walkers{display:inline-block;width:28px;height:40px;vertical-align:-3px;margin:0 1px;
    background:linear-gradient(90deg,var(--walker-a) 0 50%,var(--walker-b) 50% 100%);
    border-radius:4px}

  .band{position:absolute;color:#fff;font-family:"Roboto Condensed",sans-serif;
    white-space:nowrap;display:flex;align-items:center;justify-content:flex-end}
  .band-join{left:370px;right:16px;top:352px;height:27px;background:var(--sky);
    font-size:19px;padding-right:8px}
  .band-day{left:262px;right:16px;top:382px;height:31px;background:var(--navy);
    font-size:20px;padding-right:8px;
    clip-path:polygon(10px 0,100% 0,100% 100%,0 100%)}

  .info-panel{position:absolute;left:0;top:427px;width:274px;height:246px;background:var(--panel)}
  .info-item{position:absolute;left:34px;display:flex;align-items:flex-start}
  .info-item.time{top:28px}
  .info-item.place{top:122px}
  .info-icon{width:48px;height:48px;border-radius:50%;flex:none;margin-top:16px;
    display:flex;align-items:center;justify-content:center;box-shadow:0 1px 2px rgba(0,0,0,.25)}
  .info-icon.calendar{background:var(--yellow)}
  .info-icon.pin{background:var(--green)}
  .info-text{margin-left:18px}
  .info-label{font-size:11px;font-style:italic;font-weight:700;letter-spacing:.5px;margin-bottom:12px}
  .info-value{font-size:15px;line-height:1.45}

  .contact{position:absolute;left:274px;top:673px;width:390px;height:267px}
  .contact-icon{position:absolute;left:64px;width:50px;height:50px;border-radius:50%;
    display:flex;align-items:center;justify-content:center;box-shadow:0 1px 3px rgba(0,0,0,.3)}
  .contact-icon.web{top:20px;background:var(--blue)}
  .contact-icon.phone{top:92px;background:var(--red)}
  .contact-text{position:absolute;left:135px;top:28px;font-size:11px;line-height:1.4}
  .contact-text strong{font-weight:700}
  .contact-text .or{margin:10px 0}

  .brand{position:absolute;left:120px;top:202px;display:flex;align-items:center}
  .brand-dot{width:30px;height:30px;border-radius:50%;background:var(--brand-dot);flex:none}
  .brand-name{margin-left:10px;font-size:17px;font-weight:700;color:var(--ink)}
  .brand-tagline{margin-left:12px;font-size:11px;color:var(--ink)}
</style>
</head>
<body>
<main class="flyer">
  <div class="photo photo-rope-line" role="img" aria-label="Young volunteers in a long line holding a white pipe on a sandy beach"></div>

  <h1 class="headline">
    <span>Think Globally,</span>
    <span class="line-two">Wa<i class="walkers" role="img" aria-label="Two walking figures"></i>k Locally.</span>
  </h1>
  <p class="band band-join">Join K7U in Santa Barbara</p>
  <p class="band band-day">on Earthwide Thirst Day for a Stroll 2 Rivers.</p>

  <section class="info-panel">
    <div class="info-item time">
      <div class="info-icon calendar">
        <svg width="24" height="24" viewBox="0 0 24 24"><rect x="3" y="5" width="18" height="16" rx="2" fill="#fff"/><rect x="3" y="5" width="18" height="5" fill="#e0463a"/><rect x="7" y="2" width="2" height="5" fill="#fff"/><rect x="15" y="2" width="2" height="5" fill="#fff"/><text x="12" y="19" font-size="8" text-anchor="middle" fill="#555" font-family="Roboto, sans-serif">21</text></svg>
      </div>
      <div class="info-text">
        <p class="info-label">TIME :</p>
        <p class="info-value">Saturday, March 21st,<br>10am - 2pm</p>
      </div>
    </div>
    <div class="info-item place">
      <div class="info-icon pin">
        <svg width="24" height="24" viewBox="0 0 24 24"><path d="M12 2a7 7 0 0 0-7 7c0 5 7 13 7 13s7-8 7-13a7 7 0 0 0-7-7z" fill="#e0463a"/><circle cx="12" cy="9" r="2.6" fill="#fff"/></svg>
      </div>
      <div class="info-text">
        <p class="info-label">LOCATION :</p>
        <p class="info-value">Merrow Fern Gardens,<br>Santa Barbara</p>
      </div>
    </div>
  </section>

  <div class="photo photo-crowd" role="img" aria-label="Large cheering crowd of families in front of a blue event tent by the sea"></div>
  <div class="photo photo-digging" role="img" aria-label="Volunteers digging a trench in the sand"></div>

  <section class="contact">
    <div class="contact-icon web">
      <svg width="26" height="22" viewBox="0 0 26 22"><rect x="1" y="2" width="24" height="18" rx="2" fill="#fff"/><rect x="1" y="2" width="24" height="4" fill="#9cc0f0"/><text x="13" y="16" font-size="6" text-anchor="middle" fill="#3b7de0" font-family="Roboto, sans-serif">www</text></svg>
    </div>
    <div class="contact-icon phone">
      <svg width="18" height="26" viewBox="0 0 18 26"><rect x="2" y="1" width="14" height="24" rx="2" fill="#333"/><rect x="4" y="4" width="10" height="16" fill="#e9e9e9"/><circle cx="9" cy="22.5" r="1.2" fill="#aaa"/></svg>
    </div>
    <div class="contact-text">
      <p>For more info check out our website:<br><strong>www.brightwellaid.org</strong>,</p>
      <p class="or">or</p>
      <p>contact our Director:<br><strong>dana@brightwellaid.org;</strong><br><strong>805 382 9046</strong></p>
    </div>
    <div class="brand">
      <span class="brand-dot" aria-hidden="true"></span>
      <p class="brand-name">Brightwell Aid</p>
      <p class="brand-tagline">A Movement of Young People</p>
    </div>
  </section>
</main>
</body>
</html>
```